Proposal Microsoft Word Template

We are looking for a professional, 5 page document to import our proposals onto. We are looking for a cover page with plenty of color and design built around and utilizing our logo. The remaining four pages should utilize our logo and have some design elements to make it stand apart from other formal proposals. We aren't sure what this looks like yet, so we are open to plenty of ideas. I will upload our logo for your use. We are a fire protection company that sells primarily to other commercial clientele.

First page will be the cover page. This should have our logo prominently placed. A place for the clients name and info.
Second page will be the Executive Summary. Smaller logo, possibly a border on this page, and a clean colorful ribbon on the footer with our information on the bottom. I do like red, blue and black for colors.

Third page will be material lists and pricing information

4th page will consist of detailed scope of work, and exclusions
Fifth page will consist of terms and conditions

Target Market(s)

Commercial Industrial Government Sectors

Requirements
Must have
• Color, clean lines and formatting.

```html
<!DOCTYPE html>
<html lang="en">
<head>
<meta charset="utf-8">
<title>Bastion Fire and Security – Proposal Template Pages</title>
<link rel="stylesheet" href="https://fonts.googleapis.com/css2?family=Anton&family=Roboto:wght@400;500&display=swap">
<style>
  :root{
    --backdrop:#5b5b5b;
    --brand-red:#c4161c;
    --ink:#111111;
    --paper:#ffffff;
    --caption:#ffffff;
    --body-text:#2a2a2a;
  }
  html,body{margin:0;padding:0;width:1200px;height:1200px;overflow:hidden;background:var(--backdrop);}
  .stage{position:relative;width:1500px;height:1500px;transform:scale(.8);transform-origin:0 0;font-family:"Roboto",Arial,sans-serif;}
  .page{position:absolute;width:445px;height:624px;background:var(--paper);overflow:hidden;box-shadow:0 2px 6px rgba(0,0,0,.35);}
  .page-art{position:absolute;inset:0;width:100%;height:100%;}
  .page--cover{left:105px;top:62px;}
  .page--summary{left:937px;top:62px;}
  .page--terms{left:535px;top:756px;}
  .page-caption{position:absolute;color:var(--caption);font-size:36px;font-family:"Roboto",Arial,sans-serif;transform:translateX(-50%);}

  .wordmark{position:absolute;color:var(--paper);font-family:"Anton",Impact,sans-serif;font-weight:400;line-height:1;}
  .wordmark__name{display:block;}
  .wordmark__tag{display:block;}
  .cover-mark{left:27px;top:30px;}
  .cover-mark .wordmark__name{font-size:40px;letter-spacing:3px;}
  .cover-mark .wordmark__tag{font-size:13px;letter-spacing:3.4px;margin-top:3px;}
  .footer-mark{left:27px;top:585px;}
  .footer-mark .wordmark__name{font-size:15px;letter-spacing:1.2px;}
  .footer-mark .wordmark__tag{font-size:5.5px;letter-spacing:1.6px;margin-top:1px;}

  .cover-title{position:absolute;left:13px;top:272px;margin:0;color:var(--paper);font-family:"Anton",Impact,sans-serif;font-weight:400;font-size:42px;line-height:52px;}
  .client-fields{position:absolute;left:55px;top:483px;width:300px;font-size:12px;color:var(--ink);}
  .client-field{display:flex;align-items:flex-end;height:29px;}
  .client-field__label{white-space:nowrap;margin-right:6px;}
  .client-field__line{flex:1;border-bottom:1.5px dotted #555;margin-bottom:3px;}
  .client-field--info{padding-left:3px;}
  .web{position:absolute;font-size:12px;letter-spacing:1.6px;}
  .cover-web{left:0;right:0;top:593px;text-align:center;color:var(--ink);}
  .footer-web{right:15px;top:587px;color:var(--paper);font-size:12.5px;}

  .page-number{position:absolute;right:19px;top:11px;font-size:6.5px;color:var(--body-text);}
  .page-heading{position:absolute;left:26px;top:32px;margin:0;color:var(--brand-red);font-family:"Anton",Impact,sans-serif;font-weight:400;font-size:26px;line-height:1;letter-spacing:.3px;}
  .heading-rule{position:absolute;left:17px;top:66px;width:238px;height:4px;background:var(--ink);}
  .page--terms .heading-rule{left:21px;width:233px;}

  .copy{position:absolute;margin:0;font-size:7px;line-height:8.7px;}
  .copy--dark{color:var(--body-text);}
  .copy--light{color:var(--paper);}
  .summary-intro{left:16px;top:86px;width:416px;font-size:7.4px;line-height:10.2px;}
  .summary-block-a{left:16px;top:140px;width:244px;}
  .summary-block-b{left:16px;top:230px;width:244px;}
  .summary-block-c{left:238px;top:317px;width:126px;}
  .summary-block-d{left:301px;top:426px;width:122px;}

  .terms-list{position:absolute;left:0;top:0;margin:0;padding:0;list-style:none;}
  .terms-item{position:absolute;left:28px;display:flex;gap:8px;}
  .terms-item svg{flex:none;width:10px;height:9px;margin-top:0;}
  .terms-item p{margin:0;font-size:6.9px;line-height:8.7px;color:var(--body-text);}
</style>
</head>
<body>
<div class="stage">

  <!-- Cover -->
  <section class="page page--cover">
    <svg class="page-art" viewBox="0 0 445 624" aria-hidden="false">
      <defs>
        <linearGradient id="coverPhotoTone" x1="0" y1="0" x2="1" y2="1">
          <stop offset="0" stop-color="#3a3a3a"/>
          <stop offset=".35" stop-color="#8c2a22"/>
          <stop offset=".6" stop-color="#c9281f"/>
          <stop offset="1" stop-color="#23344e"/>
        </linearGradient>
      </defs>
      <rect width="445" height="624" fill="var(--ink)"/>
      <polygon points="445,40 445,486 195,380 165,396 165,213" fill="url(#coverPhotoTone)" role="img" aria-label="Photo of a technician holding a red fire extinguisher beside red sprinkler pipework"/>
      <polygon points="0,0 405,0 0,250" fill="var(--brand-red)"/>
      <polygon points="0,490 195,380 445,486 445,624 0,624" fill="var(--paper)"/>
    </svg>
    <div class="wordmark cover-mark">
      <span class="wordmark__name">BASTION</span>
      <span class="wordmark__tag">FIRE AND SECURITY</span>
    </div>
    <h1 class="cover-title">Title of<br>Project</h1>
    <div class="client-fields">
      <div class="client-field"><span class="client-field__label">Name -</span><span class="client-field__line"></span></div>
      <div class="client-field client-field--info"><span class="client-field__label">Info -</span><span class="client-field__line"></span></div>
      <div class="client-field client-field--info"><span class="client-field__label">Info -</span><span class="client-field__line"></span></div>
    </div>
    <div class="web cover-web">www.companyname.com</div>
  </section>
  <div class="page-caption" style="left:317px;top:714px;">Page 1</div>

  <!-- Executive Summary -->
  <section class="page page--summary">
    <svg class="page-art" viewBox="0 0 445 624">
      <defs>
        <linearGradient id="summaryCornerTone" x1="0" y1="0" x2="1" y2="1">
          <stop offset="0" stop-color="#f2f2f2"/>
          <stop offset="1" stop-color="#9a9a9a"/>
        </linearGradient>
        <radialGradient id="summaryDetectorTone" cx=".45" cy=".5" r=".7">
          <stop offset="0" stop-color="#f1c9c6"/>
          <stop offset=".4" stop-color="#d9a6a2"/>
          <stop offset="1" stop-color="#8f8582"/>
        </radialGradient>
      </defs>
      <polygon points="0,128 273,128 444,438 444,573 0,573" fill="var(--brand-red)"/>
      <polygon points="273,128 444,128 444,438" fill="url(#summaryCornerTone)" role="img" aria-label="Pale grey abstract background photo"/>
      <polygon points="0,308 183,308 333,573 0,573" fill="url(#summaryDetectorTone)" role="img" aria-label="Photo of a hand pressing the test button on a ceiling smoke detector glowing red"/>
      <rect x="0" y="573" width="445" height="51" fill="var(--ink)"/>
    </svg>
    <div class="page-number">Page 2</div>
    <h2 class="page-heading">Executive Summary</h2>
    <div class="heading-rule"></div>
    <p class="copy copy--dark summary-intro">A clear overview of the proposed fire protection work, the site needs we found, and the approach our team will take to deliver a safe and compliant system on time and within budget.</p>
    <p class="copy copy--light summary-block-a">This proposal covers the design, supply and installation of fire detection and suppression systems for your facility. Our team reviewed the site, current equipment and local code requirements. The work plan below sets out each stage, from survey and drawings through testing, handover and staff training, so your building stays protected and inspection ready at every step of the project.</p>
    <p class="copy copy--light summary-block-b">All work is carried out by certified technicians using listed equipment. Every device is tested and documented before handover, and a full maintenance plan is included so your systems remain reliable and compliant year after year.</p>
    <p class="copy copy--light summary-block-c">Our alarm panels link smoke, heat and flow sensors into one monitored network with clear alerts and quick response.</p>
    <p class="copy copy--light summary-block-d">Sprinkler and hose systems are sized to your floor plan, inspected on schedule and kept ready for use.</p>
    <div class="wordmark footer-mark">
      <span class="wordmark__name">BASTION</span>
      <span class="wordmark__tag">FIRE AND SECURITY</span>
    </div>
    <div class="web footer-web">www.companyname.com</div>
  </section>
  <div class="page-caption" style="left:1146px;top:700px;">Page 2</div>

  <!-- Terms & Conditions -->
  <section class="page page--terms">
    <svg class="page-art" viewBox="0 0 445 624">
      <defs>
        <linearGradient id="termsRoomTone" x1="0" y1="0" x2="1" y2="0">
          <stop offset="0" stop-color="#d9d9d7"/>
          <stop offset=".5" stop-color="#e8e7e4"/>
          <stop offset=".6" stop-color="#d23a30"/>
          <stop offset=".72" stop-color="#e4e3e0"/>
          <stop offset="1" stop-color="#cfcfcc"/>
        </linearGradient>
      </defs>
      <polygon points="0,378 293,378 352,307 444,307 444,572 0,572" fill="var(--brand-red)"/>
      <polygon points="0,392 301,392 360,321 444,321 444,572 0,572" fill="url(#termsRoomTone)" role="img" aria-label="Photo of a white corridor with an exit door and a red wall-mounted fire hose cabinet"/>
      <rect x="0" y="572" width="445" height="52" fill="var(--ink)"/>
    </svg>
    <div class="page-number">Page 5</div>
    <h2 class="page-heading">Terms &amp; Conditions</h2>
    <div class="heading-rule"></div>
    <ul class="terms-list">
      <li class="terms-item" style="top:86px;width:396px;">
        <svg viewBox="0 0 10 9"><path d="M1 5 L4 8 L9 1" fill="none" stroke="var(--brand-red)" stroke-width="1.8"/></svg>
        <p>Prices are valid for thirty days from the date of this proposal. Work begins once a signed copy and deposit are received. Any change to the agreed scope will be quoted in writing before work continues, and added costs must be approved by the client. Final payment is due on completion and handover of all test records.</p>
      </li>
      <li class="terms-item" style="top:145px;width:396px;">
        <svg viewBox="0 0 10 9"><path d="M1 5 L4 8 L9 1" fill="none" stroke="var(--brand-red)" stroke-width="1.8"/></svg>
        <p>The client will provide clear access to all work areas during normal hours. Delays caused by other trades, site conditions or locked areas may change the schedule. Materials remain our property until paid in full, and any damaged or missing items after delivery are the responsibility of the client.</p>
      </li>
      <li class="terms-item" style="top:208px;width:396px;">
        <svg viewBox="0 0 10 9"><path d="M1 5 L4 8 L9 1" fill="none" stroke="var(--brand-red)" stroke-width="1.8"/></svg>
        <p>All equipment carries the maker's warranty, and our labour is covered for one year from completion. The warranty does not cover misuse, tampering, water damage or repairs made by others. Inspection and testing are scheduled as set out in the service plan and follow local fire code rules.</p>
      </li>
      <li class="terms-item" style="top:268px;width:396px;">
        <svg viewBox="0 0 10 9"><path d="M1 5 L4 8 L9 1" fill="none" stroke="var(--brand-red)" stroke-width="1.8"/></svg>
        <p>Permits and fees required by the local authority are included unless noted. Any extra inspections requested by the authority will be billed at standard rates.</p>
      </li>
      <li class="terms-item" style="top:310px;width:266px;">
        <svg viewBox="0 0 10 9"><path d="M1 5 L4 8 L9 1" fill="none" stroke="var(--brand-red)" stroke-width="1.8"/></svg>
        <p>Either party may cancel with written notice. Work already done and materials ordered will be charged at cost.</p>
      </li>
      <li class="terms-item" style="top:355px;width:250px;">
        <svg viewBox="0 0 10 9"><path d="M1 5 L4 8 L9 1" fill="none" stroke="var(--brand-red)" stroke-width="1.8"/></svg>
        <p>This agreement follows the laws of the state of work.</p>
      </li>
    </ul>
    <div class="wordmark footer-mark" style="top:584px;">
      <span class="wordmark__name">BASTION</span>
      <span class="wordmark__tag">FIRE AND SECURITY</span>
    </div>
    <div class="web footer-web">www.companyname.com</div>
  </section>
  <div class="page-caption" style="left:753px;top:1390px;">Page 5</div>

</div>
</body>
</html>
```